Modern Design Business Card industrial maintenance company

Business card design for Company named Brookvale Equipment Services

Target Market(s)

Industrial

Industry/Entity Type

Maintenance and repair

Contact Information for Business Card

Place holder for address, office phone, mobile number and email

Requirements
Must have
• Clean modern look
Nice to have
• N/a

```html
<!DOCTYPE html>
<html lang="en">
<head>
<meta charset="utf-8">
<title>Brookvale Equipment Services – Business Card</title>
<link rel="stylesheet" href="https://fonts.googleapis.com/css2?family=Montserrat:wght@400;600;700&display=swap">
<style>
  :root {
    --backdrop: #9a8a72;
    --card: #1b1b1b;
    --ink: #ffffff;
    --ink-soft: #e6e6e6;
    --ring-light: #8c8c8c;
    --ring-dark: #0e0e0e;
  }
  html, body {
    margin: 0;
    padding: 0;
    width: 900px;
    height: 1200px;
    overflow: hidden;
    background: var(--backdrop);
    font-family: "Montserrat", Arial, sans-serif;
  }
  .canvas {
    position: relative;
    width: 900px;
    height: 1200px;
  }
  .card {
    position: absolute;
    width: 742px;
    height: 440px;
    background: var(--card);
    border-radius: 22px;
    overflow: hidden;
    box-shadow: 0 10px 24px rgba(0,0,0,0.45);
  }
  .card--front { left: 80px; top: 132px; }
  .card--back  { left: 79px; top: 638px; }

  .ring {
    position: absolute;
    width: 420px;
    height: 420px;
  }
  .card--front .ring { left: 485px; top: 5px; }
  .card--back .ring  { left: 322px; top: 0px; }

  .wordmark {
    position: absolute;
    color: var(--ink);
    font-weight: 600;
    line-height: 1;
  }
  .wordmark__name {
    display: block;
    font-size: 27px;
    letter-spacing: 1.5px;
  }
  .wordmark__tag {
    display: block;
    font-size: 10.5px;
    letter-spacing: 4.6px;
    margin-top: 5px;
  }
  .card--front .wordmark { left: 34px; top: 54px; }
  .card--back .wordmark  { left: 33px; top: 356px; }

  .person {
    position: absolute;
    left: 35px;
    top: 144px;
    color: var(--ink);
  }
  .person__name {
    margin: 0;
    font-size: 25px;
    font-weight: 700;
    line-height: 1.2;
  }
  .person__role {
    margin: 4px 0 0;
    font-size: 15.5px;
    font-weight: 400;
    color: var(--ink-soft);
  }
  .address {
    position: absolute;
    left: 38px;
    top: 229px;
    margin: 0;
    font-style: normal;
    font-size: 16px;
    line-height: 20px;
    color: var(--ink-soft);
  }
  .contacts {
    position: absolute;
    left: 39px;
    top: 304px;
    margin: 0;
    padding: 0;
    list-style: none;
    font-size: 16px;
    color: var(--ink-soft);
  }
  .contacts li {
    display: flex;
    align-items: center;
    height: 26px;
  }
  .contacts li:first-child { margin-bottom: 5px; }
  .contacts svg {
    width: 16px;
    height: 16px;
    margin-right: 10px;
    fill: var(--ink);
    flex: none;
  }
</style>
</head>
<body>
<main class="canvas">

  <section class="card card--front" aria-label="Business card front">
    <svg class="ring" viewBox="0 0 420 420" aria-hidden="true">
      <defs>
        <linearGradient id="ringFrontGloss" x1="0" y1="0" x2="1" y2="1">
          <stop offset="0" stop-color="var(--ring-light)"/>
          <stop offset="0.45" stop-color="#2a2a2a"/>
          <stop offset="1" stop-color="var(--ring-dark)"/>
        </linearGradient>
      </defs>
      <circle cx="210" cy="210" r="200" fill="none" stroke="url(#ringFrontGloss)" stroke-width="14"/>
    </svg>

    <div class="wordmark">
      <span class="wordmark__name">BROOKVALE</span>
      <span class="wordmark__tag">EQUIPMENT SERVICES</span>
    </div>

    <div class="person">
      <h1 class="person__name">Jonah Merrick</h1>
      <p class="person__role">Business Advisor</p>
    </div>

    <address class="address">450 Harbor Mill Lane, Ste<br>210 Ridgefield, OH 44021</address>

    <ul class="contacts">
      <li>
        <svg viewBox="0 0 24 24" aria-hidden="true"><path d="M6.6 10.8a15.1 15.1 0 0 0 6.6 6.6l2.2-2.2c.3-.3.7-.4 1-.2 1.1.4 2.3.6 3.6.6.6 0 1 .4 1 1V20c0 .6-.4 1-1 1C10.6 21 3 13.4 3 4c0-.6.4-1 1-1h3.5c.6 0 1 .4 1 1 0 1.3.2 2.5.6 3.6.1.3 0 .7-.2 1z"/></svg>
        (555) 214-3380
      </li>
      <li>
        <svg viewBox="0 0 24 24" aria-hidden="true"><path d="M8 1h8a2 2 0 0 1 2 2v18a2 2 0 0 1-2 2H8a2 2 0 0 1-2-2V3a2 2 0 0 1 2-2zm0 3v14h8V4zm4 15.5a1.2 1.2 0 1 0 0 2.4 1.2 1.2 0 0 0 0-2.4z"/></svg>
        (555) 730-6147
      </li>
      <li>
        <svg viewBox="0 0 24 24" aria-hidden="true"><path d="M2 6h20v12H2zm1.5 1 8.5 6 8.5-6z"/></svg>
        info@brookvale.com
      </li>
      <li>
        <svg viewBox="0 0 24 24" aria-hidden="true"><path d="M12 2a10 10 0 1 0 0 20 10 10 0 0 0 0-20zm-1 17.9A8 8 0 0 1 4.1 10l4.9 4.9v1a2 2 0 0 0 2 2zm6.9-2.5A2 2 0 0 0 16 16h-1v-3a1 1 0 0 0-1-1H8v-2h2a1 1 0 0 0 1-1V7h2a2 2 0 0 0 2-2v-.4a8 8 0 0 1 2.9 12.8z"/></svg>
        www.brookvale.com
      </li>
    </ul>
  </section>

  <section class="card card--back" aria-label="Business card back">
    <svg class="ring" viewBox="0 0 420 420" aria-hidden="true">
      <defs>
        <linearGradient id="ringBackGloss" x1="0" y1="0" x2="1" y2="1">
          <stop offset="0" stop-color="var(--ring-light)"/>
          <stop offset="0.45" stop-color="#2a2a2a"/>
          <stop offset="1" stop-color="var(--ring-dark)"/>
        </linearGradient>
      </defs>
      <circle cx="210" cy="210" r="200" fill="none" stroke="url(#ringBackGloss)" stroke-width="14"/>
    </svg>

    <div class="wordmark">
      <span class="wordmark__name">BROOKVALE</span>
      <span class="wordmark__tag">EQUIPMENT SERVICES</span>
    </div>
  </section>

</main>
</body>
</html>
```